Property maintenance company needs an eye catching postcard design

We are a property maintenance company that wants to send out a postcard targeting residential homeowners only. We want the postcard to create the impression of a friendly and inviting company that makes maintenance easy for homeowners. I have attached all the instructions in a pdf file as well as any other needed pictures or info. Please read the outline I provided. I also attached pictures/screenshots of our new (in progress) website if you wish to get a feel for our company.

Thanks!

Target Market(s)

residential homeowners, homeowners

Industry/Entity Type

Property Maintenance

```html
<!DOCTYPE html>
<html lang="en">
<head>
<meta charset="utf-8">
<title>Brightwell Postcard</title>
<link href="https://fonts.googleapis.com/css2?family=Montserrat:wght@500;600;700;800&display=swap" rel="stylesheet">
<style>
:root{
  --blue:#0b2887;
  --green:#76c743;
  --green-text:#7cc544;
  --white:#ffffff;
  --bg:#e4e4e4;
  --ink:#111111;
  --badge:#1d5f78;
}
*{margin:0;padding:0;box-sizing:border-box}
html,body{width:1200px;height:1200px;overflow:hidden;background:var(--bg);font-family:'Montserrat',sans-serif}
.postcard{position:absolute;width:755px;height:503px;background:var(--white)}
.front{left:71px;top:48px}
.back{left:342px;top:605px}
.abs{position:absolute}

/* front */
.hero-photo{left:9px;top:7px;width:501px;height:282px;
  clip-path:polygon(0 0,100% 0,391px 100%,0 100%);
  background:linear-gradient(180deg,#d6dde4 0%,#b9bdbf 22%,#8a847a 45%,#6f6a60 62%,#5e8f38 80%,#4f8a2e 100%)}
.brand{display:flex;align-items:center;gap:8px;color:var(--blue);font-weight:700;letter-spacing:0.5px}
.brand-dot{width:14px;height:14px;border-radius:50%;background:var(--green)}
.front .brand{left:520px;top:94px;width:216px;justify-content:center;font-size:30px}
.headline-panel{left:407px;top:163px;width:337px;height:125px;background:var(--blue);
  clip-path:polygon(53px 0,100% 0,100% 100%,0 100%)}
.headline{right:19px;top:182px;text-align:right}
.headline-main{color:var(--white);font-weight:800;font-size:24px;line-height:26px}
.headline-sub{color:var(--green-text);font-weight:600;font-size:19.5px;line-height:21px;letter-spacing:0.3px}
.headline-rule{right:19px;top:234px;width:210px;height:2px;background:var(--green)}
.headline-note{right:19px;top:243px;text-align:right;color:var(--white);font-weight:700;font-size:14px;line-height:16px}
.service-photo{top:296px;height:148px}
.photo-floor{left:9px;width:249px;clip-path:polygon(0 0,100% 0,180px 100%,0 100%);
  background:linear-gradient(160deg,#a86a3a,#d89c5e 50%,#e9bd86)}
.photo-carpentry{left:196px;width:347px;clip-path:polygon(68px 0,100% 0,279px 100%,0 100%);
  background:linear-gradient(120deg,#c27a3a,#e0a364 50%,#b86f34)}
.photo-plumbing{left:481px;width:261px;clip-path:polygon(69px 0,100% 0,100% 100%,0 100%);
  background:linear-gradient(150deg,#d9dcde,#f0f0f0 45%,#a9b0b6)}
.contact-bar{top:450px;height:45px;display:flex;align-items:center;font-weight:800}
.bar-phone{left:9px;width:326px;background:var(--blue);color:var(--green-text);
  clip-path:polygon(0 0,100% 0,308px 100%,0 100%);padding-left:38px;font-size:27px;gap:8px}
.bar-web{left:325px;width:419px;background:var(--green);color:var(--blue);
  clip-path:polygon(18px 0,100% 0,100% 100%,0 100%);padding-left:38px;font-size:26px;gap:8px}

/* back */
.offer-panel{left:9px;top:10px;width:394px;height:220px;background:var(--blue);
  clip-path:polygon(0 0,311px 0,385px 100%,0 100%)}
.scene-photo{left:9px;top:230px;width:394px;height:272px;
  clip-path:polygon(0 0,385px 0,393px 22px,304px 272px,0 272px);
  background:linear-gradient(180deg,#5f6168 0%,#8f9288 25%,#d6d5c6 45%,#ffffff 62%)}
.chevron{left:0;top:0;width:755px;height:503px}
.section-title{left:24px;top:26px;color:var(--white);font-weight:700;font-size:20px;letter-spacing:0.3px}
.title-rule{left:25px;top:52px;width:38px;height:2px;background:var(--green)}
.offer-list{left:22px;top:60px;list-style:none;color:var(--white);font-weight:500;font-size:13.8px;line-height:18.6px}
.offer-list li{display:flex;align-items:center;gap:6px}
.trade{top:136px;width:70px;text-align:center}
.trade-badge{width:59px;height:59px;margin:0 auto;border-radius:50%;background:radial-gradient(circle at 40% 35%,#ffffff,#e3e3e3 70%,#c9c9c9);
  border:2px solid #d6d6d6;display:flex;align-items:center;justify-content:center}
.trade-label{margin-top:10px;color:var(--green-text);font-weight:700;font-size:8.8px;letter-spacing:0.2px}
.back .brand{left:60px;top:386px;width:230px;justify-content:center;font-size:30px}
.back-contact{left:0;width:330px;top:442px;text-align:center;color:var(--blue);font-weight:700;font-size:13.5px;
  display:flex;justify-content:center;align-items:center;gap:4px}
.accredit-badge{left:143px;top:465px;width:59px;height:22px;border-radius:3px;background:var(--badge)}
.stamp-box{left:659px;top:39px;width:60px;height:60px;border:2px solid var(--ink)}
</style>
</head>
<body>

<section class="postcard front">
  <div class="abs hero-photo" role="img" aria-label="Photo of a large two-storey family home with a green front lawn"></div>
  <div class="abs brand"><span class="brand-dot"></span>Brightwell</div>
  <div class="abs headline-panel"></div>
  <div class="abs headline">
    <div class="headline-main">BRIGHTWELL MAKES</div>
    <div class="headline-sub">HOME MAINTENANCE EASY</div>
  </div>
  <div class="abs headline-rule"></div>
  <div class="abs headline-note">ONE POINT OF CONTACT FOR ALL<br>YOUR PROPERTY MAINTENANCE NEEDS</div>

  <div class="abs service-photo photo-floor" role="img" aria-label="Photo of a hardwood floor being polished with a buffing machine"></div>
  <div class="abs service-photo photo-carpentry" role="img" aria-label="Photo of hands fitting a wooden window frame"></div>
  <div class="abs service-photo photo-plumbing" role="img" aria-label="Photo of a plumber tightening a sink drain pipe with a wrench"></div>

  <div class="abs contact-bar bar-phone">
    <svg width="24" height="24" viewBox="0 0 24 24" fill="none" stroke="currentColor" stroke-width="2.4" stroke-linecap="round" stroke-linejoin="round"><path d="M5 3h4l2 5-3 2a12 12 0 0 0 6 6l2-3 5 2v4a2 2 0 0 1-2 2A17 17 0 0 1 3 5a2 2 0 0 1 2-2z"/><path d="M15 3a6 6 0 0 1 6 6M15 7a2 2 0 0 1 2 2"/></svg>
    403-555-0142
  </div>
  <div class="abs contact-bar bar-web">
    <svg width="24" height="24" viewBox="0 0 24 24" fill="none" stroke="currentColor" stroke-width="2"><circle cx="12" cy="12" r="10"/><path d="M2 12h20M12 2c3 3 3 17 0 20M12 2c-3 3-3 17 0 20"/></svg>
    www.brightwellpro.com
  </div>
</section>

<section class="postcard back">
  <div class="abs offer-panel"></div>
  <div class="abs scene-photo" role="img" aria-label="Photo of a worker on a ladder cleaning a house gutter"></div>
  <svg class="abs chevron" viewBox="0 0 755 503" aria-hidden="true">
    <polygon points="320,10 348,10 431,252 343,502 313,502 402,252" fill="#76c743"/>
  </svg>

  <h2 class="abs section-title">WHAT WE DO:</h2>
  <div class="abs title-rule"></div>
  <ul class="abs offer-list">
    <li><svg width="12" height="12" viewBox="0 0 12 12" fill="none" stroke="#76c743" stroke-width="1.3"><circle cx="6" cy="6" r="5.2"/><path d="M3.5 6.2l1.7 1.6 3.3-3.4"/></svg>Maintenance Packages</li>
    <li><svg width="12" height="12" viewBox="0 0 12 12" fill="none" stroke="#76c743" stroke-width="1.3"><circle cx="6" cy="6" r="5.2"/><path d="M3.5 6.2l1.7 1.6 3.3-3.4"/></svg>General Maintenance/ Handyman Repairs</li>
    <li><svg width="12" height="12" viewBox="0 0 12 12" fill="none" stroke="#76c743" stroke-width="1.3"><circle cx="6" cy="6" r="5.2"/><path d="M3.5 6.2l1.7 1.6 3.3-3.4"/></svg>Home Renovations</li>
  </ul>

  <div class="abs trade" style="left:18px">
    <div class="trade-badge"><svg width="30" height="30" viewBox="0 0 30 30" fill="none" stroke="#76c743" stroke-width="2.6" stroke-linecap="round"><circle cx="15" cy="15" r="12"/><path d="M11 19l8-8M14 10l6 6M10 20l-3 3"/></svg></div>
    <div class="trade-label">ELECTRICAL</div>
  </div>
  <div class="abs trade" style="left:85px">
    <div class="trade-badge"><svg width="32" height="30" viewBox="0 0 32 30" fill="#76c743"><circle cx="16" cy="12" r="8"/><rect x="4" y="19" width="24" height="4"/></svg></div>
    <div class="trade-label">MILLWORK</div>
  </div>
  <div class="abs trade" style="left:154px">
    <div class="trade-badge"><svg width="32" height="30" viewBox="0 0 32 30" fill="none" stroke="#76c743" stroke-width="3" stroke-linecap="round"><path d="M13 6l12 12M10 9l6-6"/><rect x="5" y="22" width="22" height="4" fill="#76c743" stroke="none"/></svg></div>
    <div class="trade-label">FLOORING</div>
  </div>
  <div class="abs trade" style="left:222px">
    <div class="trade-badge"><svg width="30" height="30" viewBox="0 0 30 30" fill="none" stroke="#76c743" stroke-width="3.2" stroke-linecap="round"><path d="M6 6l18 18M24 6L6 24"/></svg></div>
    <div class="trade-label">CARPENTRY</div>
  </div>
  <div class="abs trade" style="left:290px">
    <div class="trade-badge"><svg width="30" height="30" viewBox="0 0 30 30" fill="none" stroke="#76c743" stroke-width="3" stroke-linecap="round"><path d="M7 26V10h12v6M13 10V5M9 5h8"/><path d="M19 20c-2 3-2 4 0 5 2-1 2-2 0-5z" fill="#76c743"/></svg></div>
    <div class="trade-label">PLUMBING</div>
  </div>

  <div class="abs brand"><span class="brand-dot"></span>Brightwell</div>
  <div class="abs back-contact">
    <svg width="12" height="12" viewBox="0 0 24 24" fill="none" stroke="#76c743" stroke-width="2.6" stroke-linecap="round" stroke-linejoin="round"><path d="M5 3h4l2 5-3 2a12 12 0 0 0 6 6l2-3 5 2v4a2 2 0 0 1-2 2A17 17 0 0 1 3 5a2 2 0 0 1 2-2z"/></svg>
    403-555-0142 |
    <svg width="12" height="12" viewBox="0 0 24 24" fill="none" stroke="#76c743" stroke-width="2.2"><circle cx="12" cy="12" r="10"/><path d="M2 12h20M12 2c3 3 3 17 0 20M12 2c-3 3-3 17 0 20"/></svg>
    www.brightwellpro.com
  </div>
  <div class="abs accredit-badge"></div>

  <div class="abs stamp-box"></div>
</section>

</body>
</html>
```